Brantley Water Taxi and Transport

Need to redesign our business cards to relay that we do freight logistics and water taxi service. We also work with gov. agencies doing environmental clean up, oil spill response, remote site construction and work with many of the air taxi and helicopter services on Kodiak Island. Out website is www.brantleywatertaxi-example.com to get a better idea of what we do.

Contact Information for Business Card

I have a previous business card but it just has the logo on the front, and a sunset picture on the back with the contact info. It does not relay what we do and what we can help with. I like a simple straight forward design over a busy one.

Colors
3176b5
0455a3
cfdfed

Requirements
Must have
• logo, email, website, phone number

```html
<!DOCTYPE html>
<html lang="en">
<head>
<meta charset="UTF-8">
<title>Brantley Water Taxi and Transport — Business Card</title>
<link href="https://fonts.googleapis.com/css2?family=Oswald:wght@500&family=Open+Sans:wght@400;600&family=Montserrat:wght@700&display=swap" rel="stylesheet">
<style>
  :root {
    --blue-mid: #3176b5;
    --blue-deep: #0455a3;
    --blue-pale: #cfdfed;
    --navy: #1d2f73;
    --ink: #1b1b1f;
    --paper: #ffffff;
    --stage: #e9edf2;
  }
  * { box-sizing: border-box; margin: 0; padding: 0; }
  html, body { width: 1200px; height: 900px; overflow: hidden; }
  body {
    background: var(--stage);
    font-family: "Open Sans", sans-serif;
    position: relative;
  }
  .card {
    position: absolute;
    left: 250px;
    width: 700px;
    height: 400px;
    overflow: hidden;
    box-shadow: 0 6px 18px rgba(20, 30, 60, 0.18);
  }

  /* Front */
  .card-front { top: 40px; }
  .front-photo {
    position: absolute; inset: 0;
    background: linear-gradient(170deg, #7d97cf 0%, #4a63b3 38%, #2f4a9e 65%, #24408f 100%);
  }
  .front-content {
    position: absolute; inset: 0;
    display: flex; flex-direction: column; align-items: center; justify-content: center;
    color: var(--paper); text-align: center;
  }
  .front-mark {
    width: 46px; height: 46px; border-radius: 50%;
    background: var(--paper); margin-bottom: 14px;
  }
  .front-title {
    font-family: "Oswald", sans-serif; font-weight: 500;
    font-size: 38px; letter-spacing: 1px; text-transform: uppercase;
    white-space: nowrap;
  }
  .front-tagline {
    margin-top: 6px; font-size: 15px; letter-spacing: 0.4px;
    white-space: nowrap;
  }

  /* Back */
  .card-back { top: 460px; background: var(--paper); }
  .brand {
    position: absolute; left: 48px; top: 48px;
    display: flex; align-items: center; gap: 18px;
  }
  .brand-dot {
    width: 58px; height: 58px; border-radius: 50%; background: var(--blue-deep); flex: none;
  }
  .brand-name {
    font-family: "Montserrat", sans-serif; font-weight: 700;
    font-size: 36px; line-height: 1.05; color: var(--blue-deep);
    text-transform: uppercase; letter-spacing: 1px;
    white-space: nowrap;
  }
  .gallery { position: absolute; left: 0; top: 0; }
  .tile { position: absolute; width: 60px; height: 52px; }
  .tile-dock { background: linear-gradient(160deg, #8a97a3, #4c5560); }
  .tile-water { background: linear-gradient(180deg, #6fa8de, #1f5aa8); }
  .tile-boat { background: linear-gradient(170deg, #a9b2ba, #5a4f4c); }
  .tile-wake { background: linear-gradient(180deg, #3f7fd0, #1c4f9c); }

  .contacts {
    position: absolute; left: 334px; top: 196px;
    list-style: none; color: var(--ink); font-size: 16px;
  }
  .contacts li {
    display: flex; align-items: center; gap: 12px; height: 34px;
    white-space: nowrap;
  }
  .contacts svg { width: 18px; height: 18px; flex: none; fill: var(--navy); }
</style>
</head>
<body>

<section class="card card-front">
  <div class="front-photo" role="img" aria-label="Photo of a water taxi boat cruising across open blue water with mountains behind"></div>
  <div class="front-content">
    <div class="front-mark"></div>
    <h1 class="front-title">Brantley Water Taxi &amp; Transport</h1>
    <p class="front-tagline">Water taxi &amp; freight transport services for the Kodiak Island area</p>
  </div>
</section>

<section class="card card-back">
  <div class="brand">
    <div class="brand-dot"></div>
    <p class="brand-name">Brantley<br>Water Taxi &amp; Transport</p>
  </div>

  <div class="gallery">
    <div class="tile tile-dock" role="img" aria-label="Photo of crew on a dock" style="left:40px;top:262px;"></div>
    <div class="tile tile-boat" role="img" aria-label="Photo of boat deck with cargo" style="left:170px;top:216px;"></div>
    <div class="tile tile-dock" role="img" aria-label="Photo of crew loading freight" style="left:236px;top:208px;"></div>
    <div class="tile tile-water" role="img" aria-label="Photo of calm bay water" style="left:124px;top:284px;"></div>
    <div class="tile tile-boat" role="img" aria-label="Photo of vessel at harbor" style="left:56px;top:334px;"></div>
    <div class="tile tile-water" role="img" aria-label="Photo of shoreline from the water" style="left:136px;top:334px;"></div>
    <div class="tile tile-wake" role="img" aria-label="Photo of boat wake from the stern" style="left:246px;top:310px;"></div>
  </div>

  <ul class="contacts">
    <li>
      <svg viewBox="0 0 24 24" aria-hidden="true"><path d="M6.6 10.8a15 15 0 0 0 6.6 6.6l2.2-2.2c.3-.3.7-.4 1-.2 1.1.4 2.300.6 3.6.6.6 0 1 .4 1 1V20c0 .6-.4 1-1 1A17 17 0 0 1 3 4c0-.6.4-1 1-1h3.5c.6 0 1 .4 1 1 0 1.3.2 2.5.6 3.6.1.3 0 .7-.2 1z"/></svg>
      <span>555 014 3400</span>
    </li>
    <li>
      <svg viewBox="0 0 24 24" aria-hidden="true"><path d="M2 5h20v14H2z"/><path d="M3 6.5l9 6.5 9-6.5" fill="none" stroke="#fff" stroke-width="1.6"/></svg>
      <span>hello@brantleywatertaxi-example.com</span>
    </li>
    <li>
      <svg viewBox="0 0 24 24" aria-hidden="true"><circle cx="12" cy="12" r="8"/></svg>
      <span>/brantleywatertaxi</span>
    </li>
    <li>
      <svg viewBox="0 0 24 24" aria-hidden="true"><circle cx="12" cy="12" r="10"/><g fill="none" stroke="#fff" stroke-width="1.3"><ellipse cx="12" cy="12" rx="4" ry="10"/><path d="M2 12h20M4 7h16M4 17h16"/></g></svg>
      <span>www.brantleywatertaxi-example.com</span>
    </li>
  </ul>
</section>

</body>
</html>
```